Postcard Design

our company name is wexford lane haven.we provide face to face psychic tarot reading and crystal healing in a very exclusive and private clinic. we provide answers and guidance for future life event and the balance for the body and soul.we are base in 17 wexford lane in london .we want a card who say what we do as clear as possible and who is eye catching to people so when they see it want to read it this is our web site www.wexfordlnhaven.co.uk you need to put number on it to call us the number ContacUs:
0208 594 3216
0788 213 5072

Industry/Entity Type

Clinic

```html
<!DOCTYPE html>
<html lang="en">
<head>
<meta charset="utf-8">
<title>Wexford Lane Haven – Postcard</title>
<link rel="stylesheet" href="https://fonts.googleapis.com/css2?family=Cinzel:wght@400;600&family=Great+Vibes&family=Open+Sans:wght@400;600;700&display=swap">
<style>
  :root {
    --bg: #2a2a2a;
    --paper: #ffffff;
    --purple: #8a2a86;
    --purple-deep: #6e1c6c;
    --green: #4f8a2a;
    --green-deep: #2f6a1e;
    --teal-green: #1f7a4a;
    --gold: #c9a23a;
    --gold-light: #e7c86a;
    --ink: #3a3a3a;
    --muted: #555555;
  }
  * { box-sizing: border-box; margin: 0; padding: 0; }
  html, body { width: 1200px; height: 1200px; overflow: hidden; background: var(--bg); }
  .canvas { position: relative; width: 1200px; height: 1200px; }

  /* ---------- Back side ---------- */
  .card-back {
    position: absolute; left: 400px; top: 40px; width: 760px; height: 580px;
    background: var(--paper); font-family: "Open Sans", sans-serif;
  }
  .about-panel {
    position: absolute; left: 14px; top: 14px; width: 380px; height: 380px;
    background: var(--purple);
  }
  .about-text {
    position: absolute; left: 14px; top: 14px; width: 248px;
    color: #fff; font-size: 14px; line-height: 18px; text-align: justify;
  }
  .drop-cap {
    float: left; font-family: "Great Vibes", cursive; color: var(--gold-light);
    font-size: 72px; line-height: 56px; margin: 2px 6px 0 0;
  }
  .photo-column { position: absolute; left: 272px; top: 0; width: 108px; height: 380px; background: var(--purple-deep); }
  .photo-frame {
    position: absolute; left: 8px; width: 94px; height: 178px;
    border: 2px solid var(--gold);
  }
  .photo-frame.stones { top: 6px; background: linear-gradient(160deg, #8ab04a, #3b3a34 60%, #2a2a28); }
  .photo-frame.statue { top: 194px; background: radial-gradient(circle at 50% 55%, #d9a93a, #8a5a16 75%); }
  .info-band {
    position: absolute; left: 14px; top: 394px; width: 380px; height: 80px;
    background: var(--teal-green); border-top: 3px solid var(--gold); border-bottom: 3px solid var(--gold);
    color: #fff;
  }
  .social { position: absolute; left: 10px; top: 10px; font-size: 13px; }
  .social-item { display: flex; align-items: center; gap: 8px; height: 28px; }
  .social-mark { width: 20px; height: 20px; background: #ffffff; opacity: .85; }
  .info-divider { position: absolute; left: 206px; top: 10px; width: 1px; height: 54px; background: rgba(255,255,255,.7); }
  .opening { position: absolute; left: 214px; top: 6px; width: 160px; text-align: center; font-family: "Cinzel", serif; }
  .opening-title { font-size: 16px; font-weight: 600; }
  .opening-days { font-size: 12px; line-height: 15px; }
  .address {
    position: absolute; left: 420px; top: 52px; font-size: 13px; line-height: 18px; color: #222;
  }
  .address strong { font-weight: 700; font-size: 13.5px; }
  .stamp-box { position: absolute; left: 636px; top: 56px; width: 104px; height: 120px; border: 1px solid #777; }

  /* ---------- Front side ---------- */
  .card-front {
    position: absolute; left: 40px; top: 600px; width: 760px; height: 580px;
    background: var(--paper); overflow: hidden;
  }
  .masthead {
    position: absolute; left: 0; top: 0; width: 760px; height: 96px;
    background: var(--purple); border-top: 4px solid var(--gold); border-bottom: 3px solid var(--gold);
  }
  .masthead-photo { position: absolute; left: 10px; top: 6px; width: 96px; height: 78px; background: radial-gradient(circle at 40% 50%, #e0a840, #8a4a10 80%); }
  .brand-name {
    position: absolute; left: 132px; top: 14px; color: #fff;
    font-family: "Cinzel", serif; font-size: 28px; letter-spacing: 6px; white-space: nowrap;
  }
  .tagline {
    position: absolute; left: 132px; top: 56px; color: #fff;
    font-family: "Cinzel", serif; font-size: 11.5px; letter-spacing: 1.2px; white-space: nowrap;
  }
  .hero-photo {
    position: absolute; left: 0; top: 96px; width: 760px; height: 380px;
    background: linear-gradient(135deg, #b7a6cf, #8d76b0 55%, #5d4c78);
  }
  .hero-fade {
    position: absolute; left: 0; top: 96px; width: 760px; height: 380px;
    background: linear-gradient(90deg, var(--green) 0%, rgba(79,138,42,.85) 30%, rgba(79,138,42,0) 62%);
  }
  .headline {
    position: absolute; left: 14px; top: 112px; color: #fff;
    font-family: "Great Vibes", cursive; font-size: 96px; line-height: 86px;
    text-shadow: 1px 2px 3px rgba(0,0,0,.35);
  }
  .services {
    position: absolute; left: 26px; top: 334px; color: #fff;
    font-family: "Cinzel", serif; font-size: 25px; line-height: 30px; letter-spacing: 1.5px;
  }
  .swoosh { position: absolute; left: 0; top: 388px; width: 760px; height: 192px; }
  .contact {
    position: absolute; left: 22px; top: 494px; color: var(--ink);
    font-family: "Cinzel", serif; font-size: 29px; line-height: 38px; letter-spacing: 1px;
  }
  .contact .sep { margin: 0 12px; }
</style>
</head>
<body>
<div class="canvas">

  <section class="card-back" aria-label="Postcard back">
    <div class="about-panel">
      <p class="about-text"><span class="drop-cap">T</span>he Wexford Lane Haven is a brand new venture aimed at creating an oasis in the midst of the city by bringing the art of psychic readings and healing. Wexford Lane is a famous landmark and has a long history and tradition of treating the body and, to a lesser degree the mind. The haven's aim is to re-ignite the curiosity for the tarot and clairvoyance reading in helping you access answers with guidance and much more.</p>
      <div class="photo-column">
        <div class="photo-frame stones" role="img" aria-label="Photo of smooth stones, candle and flower"></div>
        <div class="photo-frame statue" role="img" aria-label="Photo of a golden seated statue"></div>
      </div>
    </div>
    <div class="info-band">
      <div class="social">
        <div class="social-item"><span class="social-mark"></span>Wexford Lane Haven</div>
        <div class="social-item"><span class="social-mark"></span>@wexfordlnhaven</div>
      </div>
      <div class="info-divider"></div>
      <div class="opening">
        <div class="opening-title">Opening Times:</div>
        <div class="opening-days">Monday, Wednesday,<br>Friday &amp; Saturday<br>10:30 - 19:00</div>
      </div>
    </div>
    <div class="address">
      <strong>WEXFORD LANE HAVEN</strong><br>
      17 Wexford Lane<br>
      London W1D 4QN
    </div>
    <div class="stamp-box"></div>
  </section>

  <section class="card-front" aria-label="Postcard front">
    <header class="masthead">
      <div class="masthead-photo" role="img" aria-label="Warm golden photo of a statue"></div>
      <div class="brand-name">WEXFORD LANE HAVEN</div>
      <div class="tagline">THE PLACE TO FIND HEALING, GUIDANCE AND ANSWERS FOR YOUR FUTURE.</div>
    </header>
    <div class="hero-photo" role="img" aria-label="Photo of tarot cards, crystals and a candle on a purple cloth"></div>
    <div class="hero-fade"></div>
    <h1 class="headline">Face to<br>Face</h1>
    <p class="services">PSYCHIC TAROT READING<br>AND CRYTAL HEALING</p>
    <svg class="swoosh" viewBox="0 0 760 192" preserveAspectRatio="none" aria-hidden="true">
      <path d="M0 40 C200 110 420 20 760 30 L760 192 L0 192 Z" fill="#ffffff"/>
      <path d="M0 40 C200 110 420 20 760 30 L760 44 C420 36 200 124 0 56 Z" fill="#3f7f25"/>
      <path d="M0 62 C220 128 430 44 760 50 L760 58 C430 54 220 136 0 70 Z" fill="#6aa83a"/>
    </svg>
    <div class="contact">
      <div>0208 594 3216<span class="sep">|</span>0788 213 5072</div>
      <div>WWW.WEXFORDLNHAVEN.CO.UK</div>
    </div>
  </section>

</div>
</body>
</html>
```